Looking for a creative label design for our retail coffee bags

We are a coffee manufacturer (coffee roaster) looking to re-brand our retail label for our coffee bags. Our main coffee blend that we sell is our Colombian Supremo Blend. You can use this name when creating the label. We are going for a look that represents our company as a coffee roaster. Please reference our website (www.brindlemoorroasters.com) and our Facebook page to learn more about our company and to give you more inspiration on creating this design.

Target Market(s)

Retail customers/grocery stores

Industry/Entity Type

Manufacturer

Requirements
Must have
• The size of the label has to be 3" width x 4" height

Logo must be Black
Nice to have
• We currently incorporate a color on our labels for each blend. For example, Colombian Supremo Blend (royal blue), Decaffeinated Blend (red), Breakfast Blend (green), Flavored coffees (gold).

Rustic/vintage style

```html
<!DOCTYPE html>
<html lang="en">
<head>
<meta charset="utf-8">
<title>Blend Labels</title>
<link href="https://fonts.googleapis.com/css2?family=Oswald:wght@400;500;600&display=swap" rel="stylesheet">
<style>
:root{
  --paper:#f8f8f8;
  --bg:#ffffff;
  --royal:#16147a;
  --royal-soft:#5b5ad0;
  --royal-tint:#c9c9ee;
  --brick:#7a1410;
  --brick-soft:#a2443c;
  --brick-tint:#e6c8c4;
  --ink:#1a1a1a;
}
*{box-sizing:border-box;margin:0;padding:0}
html,body{width:1200px;height:1000px;overflow:hidden;background:var(--bg)}
body{position:relative;font-family:"Oswald",sans-serif}
.label{position:absolute;left:152px;width:316px;background:var(--paper);border:3px solid var(--c)}
.label--supremo{--c:var(--royal);--soft:var(--royal-soft);--tint:var(--royal-tint);top:43px;height:420px}
.label--decaf{--c:var(--brick);--soft:var(--brick-soft);--tint:var(--brick-tint);top:485px;height:418px}
.label__frame{position:absolute;left:15px;right:15px;top:12px;bottom:16px;border:3px solid var(--c);display:flex;flex-direction:column}
.label__title{height:118px;display:flex;flex-direction:column;align-items:center;justify-content:center;color:var(--c);border-bottom:3px solid var(--c)}
.label__name{font-weight:600;font-size:33px;line-height:1;letter-spacing:.2px;transform:scaleX(.82)}
.label__kind{font-weight:500;font-size:17px;letter-spacing:3px;margin-top:7px}
.label__band{height:32px;background:var(--tint);border-bottom:3px solid var(--c)}
.label__roast{height:66px;display:flex;align-items:center;border-bottom:3px solid var(--c)}
.label__art{width:66px;height:100%;background:var(--soft);border-right:5px solid var(--c)}
.roast{display:flex;align-items:center;gap:8px;color:var(--c);font-weight:500;font-size:14px;line-height:1.1;padding-left:12px}
.roast__dots{display:flex;gap:3px}
.roast__dot{width:13px;height:13px;border:1.5px solid var(--c);border-radius:50%}
.roast__dot--on{background:var(--c)}
.label__body{flex:1;position:relative;padding:14px 0 0 12px}
.label__copy{width:170px;color:var(--c);font-weight:500;font-size:10.5px;line-height:19.5px;text-transform:uppercase}
.brand{position:absolute;right:10px;top:38px;width:84px;height:84px;border-radius:50%;background:var(--ink);display:flex;align-items:center;justify-content:center;color:#fff;font-weight:500;font-size:13px;letter-spacing:.5px;text-transform:uppercase}
.label--decaf .label__title{height:116px}
.label--decaf .label__roast{height:70px}
</style>
</head>
<body>

<section class="label label--supremo">
  <div class="label__frame">
    <header class="label__title">
      <h1 class="label__name">COLUMBIAN SUPREMO</h1>
      <p class="label__kind">BLEND</p>
    </header>
    <div class="label__band" role="img" aria-label="Row of alternating triangles pattern"></div>
    <div class="label__roast">
      <div class="label__art" role="img" aria-label="Sketch of a coffee branch with leaves and cherries"></div>
      <div class="roast">
        <span>LIGHT<br>ROAST</span>
        <span class="roast__dots"><i class="roast__dot"></i><i class="roast__dot"></i><i class="roast__dot"></i><i class="roast__dot roast__dot--on"></i><i class="roast__dot"></i></span>
        <span>DARK<br>ROAST</span>
      </div>
    </div>
    <div class="label__body">
      <p class="label__copy">Our finest blend is made from the best arabica beans South America has to offer, carefully roasted to perfection. Its distinctive rich aroma with a smooth Colombian undertone will leave you coming back for more.</p>
      <div class="brand">Brindlemoor</div>
    </div>
  </div>
</section>

<section class="label label--decaf">
  <div class="label__frame">
    <header class="label__title">
      <h1 class="label__name">DECAFFEINATED</h1>
      <p class="label__kind">BLEND</p>
    </header>
    <div class="label__band" role="img" aria-label="Row of vertical stripes pattern"></div>
    <div class="label__roast">
      <div class="label__art" role="img" aria-label="Sketch of roasted coffee beans"></div>
      <div class="roast">
        <span>LIGHT<br>ROAST</span>
        <span class="roast__dots"><i class="roast__dot"></i><i class="roast__dot roast__dot--on"></i><i class="roast__dot"></i><i class="roast__dot"></i><i class="roast__dot"></i></span>
        <span>DARK<br>ROAST</span>
      </div>
    </div>
    <div class="label__body">
      <p class="label__copy">Our finest blend is made from the best arabica beans South America has to offer, carefully roasted to perfection. Its distinctive rich aroma with a smooth Colombian undertone will leave you coming back for more.</p>
      <div class="brand">Brindlemoor</div>
    </div>
  </div>
</section>

</body>
</html>
```